Workbook Cover Design

I am needing the cover for a workbook designed. I have attached a sample cover along with a few images giving an idea what at I am looking for. I'm open to new color schemes. I also attached a flyer of the event to give you an idea of the current color theme. The workbook will be approximately 8.5 x 11.

Title : Stewardship Workshop 202
Lorna Pell Ministries

On the cover I would like to have four sections with the following title under each section:
Evangelism (use photo similar to hands with cross)
Praying in Tongues (Photo similar to bird with heart or one with a mouth speaking)
Authority of the Believer (Photo with badge or similar)
Healing (Photo of man and wheelchair or similar)

Using silhouettes are okay, but I prefer not to have any actual faces of people.

```html
<!DOCTYPE html>
<html lang="en">
<head>
<meta charset="utf-8">
<title>Stewardship Workshop 202 — Workbook Cover</title>
<link rel="stylesheet" href="https://fonts.googleapis.com/css2?family=Anton&family=Great+Vibes&family=Oswald:wght@600&family=Crimson+Text:wght@400;700&display=swap">
<style>
  :root {
    --purple-deep: #2a1f4a;
    --purple-mid: #5a4596;
    --purple-light: #8a76c2;
    --gold-light: #f6eeb0;
    --gold-mid: #d9b56e;
    --gold-dark: #c4954e;
    --gold-label: #e6cc88;
    --ring: #f7efba;
    --band: #e8d597;
    --ink: #2e2350;
    --white: #ffffff;
  }
  html, body { margin: 0; padding: 0; overflow: hidden; background: var(--purple-deep); }
  .cover {
    position: relative;
    width: 927px;
    height: 1200px;
    overflow: hidden;
    background:
      radial-gradient(ellipse 260px 420px at 200px 150px, rgba(160,140,210,.55), transparent 70%),
      radial-gradient(ellipse 300px 500px at 520px 720px, rgba(150,125,210,.55), transparent 70%),
      radial-gradient(ellipse 320px 600px at 860px 820px, rgba(10,8,20,.75), transparent 70%),
      radial-gradient(ellipse 280px 380px at 880px 200px, rgba(140,110,200,.5), transparent 70%),
      linear-gradient(180deg, #3d2f6a 0%, #4c3a86 45%, #5b47a0 75%, #3a2b66 100%);
  }
  .cover-art { position: absolute; inset: 0; }
  .title-script {
    font-family: "Great Vibes", cursive;
    font-size: 128px;
    fill: var(--white);
  }
  .title-main {
    font-family: "Anton", sans-serif;
    font-size: 214px;
  }
  .tagline {
    font-family: "Crimson Text", serif;
    font-size: 38px;
    fill: var(--white);
  }
  .tagline .tagline-name { font-weight: 700; }
  .sessions-word {
    font-family: "Anton", sans-serif;
    font-size: 132px;
    fill: var(--gold-label);
    letter-spacing: 2px;
  }
  .session-label {
    font-family: "Oswald", sans-serif;
    font-weight: 600;
    font-size: 24px;
    fill: var(--gold-label);
  }
  .session-ring { stroke: var(--ring); stroke-width: 5; }
  .footer-band {
    position: absolute;
    left: 0; right: 0; bottom: 0;
    height: 129px;
    background: var(--band);
    display: flex;
    align-items: center;
    justify-content: center;
  }
  .footer-name {
    margin: 0;
    font-family: "Crimson Text", serif;
    font-weight: 700;
    font-size: 70px;
    color: var(--ink);
  }
</style>
</head>
<body>
<main class="cover">
  <svg class="cover-art" width="927" height="1200" viewBox="0 0 927 1200" xmlns="http://www.w3.org/2000/svg">
    <defs>
      <linearGradient id="gold-title" x1="0" y1="0" x2="1" y2="0">
        <stop offset="0" stop-color="var(--gold-light)"/>
        <stop offset="0.5" stop-color="var(--gold-dark)"/>
        <stop offset="1" stop-color="var(--gold-light)"/>
      </linearGradient>
      <radialGradient id="photo-hands" cx="0.5" cy="0.55" r="0.6">
        <stop offset="0" stop-color="#fff6e0"/>
        <stop offset="0.45" stop-color="#d9b58a"/>
        <stop offset="1" stop-color="#5a4a40"/>
      </radialGradient>
      <radialGradient id="photo-badge" cx="0.5" cy="0.5" r="0.55">
        <stop offset="0" stop-color="#b8904a"/>
        <stop offset="0.4" stop-color="#3a2e1a"/>
        <stop offset="1" stop-color="#0a0a0a"/>
      </radialGradient>
      <radialGradient id="photo-dove" cx="0.5" cy="0.5" r="0.6">
        <stop offset="0" stop-color="#f2a040"/>
        <stop offset="0.5" stop-color="#a8381a"/>
        <stop offset="1" stop-color="#2a0c08"/>
      </radialGradient>
      <radialGradient id="photo-healing" cx="0.7" cy="0.6" r="0.7">
        <stop offset="0" stop-color="#ffd890"/>
        <stop offset="0.5" stop-color="#c9773a"/>
        <stop offset="1" stop-color="#3a2418"/>
      </radialGradient>
    </defs>

    <text class="title-script" x="463" y="172" text-anchor="middle">Stewardship</text>
    <text class="title-main" x="80" y="378" textLength="786" lengthAdjust="spacingAndGlyphs" fill="url(#gold-title)">WORKSHOP 202</text>

    <text class="tagline" x="473" y="432" text-anchor="middle">A learn and do workshop with <tspan class="tagline-name">Lorna Pell Ministries</tspan></text>

    <text class="sessions-word" transform="translate(238 977) rotate(-90)" textLength="464" lengthAdjust="spacingAndGlyphs">SESSIONS</text>

    <text class="session-label" x="372" y="510" text-anchor="middle">EVANGELISM</text>
    <text class="session-label" x="659" y="510" text-anchor="middle">AUTHORITY OF THE BELIEVER</text>

    <circle class="session-ring" cx="372" cy="650" r="106" fill="url(#photo-hands)" role="img" aria-label="Photo: open hands raised toward a glowing cross in the sky"/>
    <circle class="session-ring" cx="648" cy="637" r="106" fill="url(#photo-badge)" role="img" aria-label="Photo: gold security officer badge on a black background"/>
    <circle class="session-ring" cx="379" cy="870" r="106" fill="url(#photo-dove)" role="img" aria-label="Photo: white dove flying through a heart of flames"/>
    <circle class="session-ring" cx="656" cy="868" r="106" fill="url(#photo-healing)" role="img" aria-label="Photo: silhouette standing with raised arms beside an empty wheelchair at sunset"/>

    <text class="session-label" x="383" y="1024" text-anchor="middle">PRAYING IN TONGUES</text>
    <text class="session-label" x="674" y="1024" text-anchor="middle">HEALING</text>
  </svg>

  <footer class="footer-band">
    <p class="footer-name">Lorna Pell Ministries</p>
  </footer>
</main>
</body>
</html>
```